New Business Card Design for Engineering and Surveying Company

We need a new design template for our business cards. We are a civil engineering, land surveying and pipeline integrity business. Please see brqholt.com for details. We need a bold, new business card design to complement our rebranding and marketing program. We have anew logo and attached vectro file. Please find additional details below. I am available to answer any questions.

Target Market(s)

Contractors, business owners, oil companies

Contact Information for Business Card

Needs to be customizable for different people (name, title, cell)

Font styles to use
Sans Serif
Other font styles liked:
• See eps file

Requirements
Must have
• Example Information:
Derek Fannaby

T:555-318-0187
M: 555-274-0143
dfannaby@brqholt.com

Address: 1870 Corvane Parkway, Halvern, Oregon 77701
Email: dfanbagy@brqholt.com
Website: www.brqholt.com
Nice to have
• I would like the back of the card to have the logo on a bold background with the text below:

[logo]
ROLAND FANNABY & ASSOCIATES
CIVIL ENGINEERING | LAND SURVEYING | PIPELINE INTEGRITY

The reverse side should have the contact information for the person (example above), a smaller version of the logo and a graphic

```html
<!DOCTYPE html>
<html lang="en">
<head>
<meta charset="utf-8">
<title>RFA Business Card</title>
<link rel="stylesheet" href="https://fonts.googleapis.com/css2?family=Lato:wght@400;700;900&display=swap">
<style>
  :root {
    --backdrop: #d1d1cc;
    --card: #262527;
    --edge: #e21b2c;
    --brand-blue: #2853b4;
    --text-light: #f2f2f2;
    --text-muted: #d6d6d6;
  }
  * { box-sizing: border-box; margin: 0; padding: 0; }
  html, body {
    width: 1200px; height: 801px; overflow: hidden;
    background: var(--backdrop);
    font-family: 'Lato', sans-serif;
  }
  .stage { position: relative; width: 1200px; height: 801px; }
  .card {
    position: absolute; top: 249px;
    width: 530px; height: 303px;
    background: var(--card);
    border-bottom: 5px solid var(--edge);
    overflow: hidden;
  }
  .card--front { left: 50px; }
  .card--back { left: 620px; }

  .brand {
    position: absolute; display: flex; align-items: center; gap: 12px;
    color: var(--text-light); font-weight: 900; letter-spacing: 1px; line-height: 1;
  }
  .card--front .brand { left: 38px; top: 86px; font-size: 58px; }
  .brand__mark { width: 22px; height: 22px; background: var(--edge); }

  .divider {
    position: absolute; left: 228px; top: 30px;
    width: 1.5px; height: 150px; background: var(--edge);
  }

  .contact { position: absolute; left: 250px; top: 28px; color: var(--text-light); }
  .contact__name { color: var(--brand-blue); font-weight: 900; font-size: 27px; line-height: 1.05; }
  .contact__title { font-size: 14px; margin-top: 3px; }
  .contact__address { font-size: 13px; line-height: 1.35; margin-top: 12px; }
  .contact__list { list-style: none; margin-top: 8px; font-size: 13px; line-height: 1.4; }
  .contact__list li { display: flex; align-items: center; gap: 8px; }
  .contact__list svg { width: 12px; height: 12px; flex: none; fill: var(--edge); }

  .tagline {
    position: absolute; left: 38px; right: 20px; top: 222px;
    color: var(--text-muted); font-size: 13.5px; letter-spacing: 1.2px; line-height: 1.5;
    text-transform: uppercase;
  }
  .tagline__line--second { padding-left: 58px; }

  .card--back .brand { right: 40px; bottom: 48px; font-size: 92px; }
</style>
</head>
<body>
<main class="stage">
  <section class="card card--front" aria-label="Business card, contact side">
    <div class="brand"><span class="brand__mark"></span><span class="brand__name">RFA</span></div>
    <div class="divider"></div>
    <div class="contact">
      <h1 class="contact__name">Derek Fannaby</h1>
      <p class="contact__title">Founder &amp; CEO</p>
      <p class="contact__address">1870 Corvane Parkway,<br>Halvern, Oregon 77701</p>
      <ul class="contact__list">
        <li><svg viewBox="0 0 12 12" aria-hidden="true"><path d="M2.5 0.5 L4.5 0.5 L5.3 3 L4 4.2 C4.7 5.8 6.2 7.3 7.8 8 L9 6.7 L11.5 7.5 L11.5 9.5 C11.5 10.6 10.6 11.5 9.5 11.5 C4.5 11.2 0.8 7.5 0.5 2.5 C0.5 1.4 1.4 0.5 2.5 0.5 Z"/></svg>555-318-0187</li>
        <li><svg viewBox="0 0 12 12" aria-hidden="true"><path d="M3 0.5 H9 A1 1 0 0 1 10 1.5 V10.5 A1 1 0 0 1 9 11.5 H3 A1 1 0 0 1 2 10.5 V1.5 A1 1 0 0 1 3 0.5 Z M3.5 2 V9 H8.5 V2 Z"/></svg>555-274-0143</li>
        <li><svg viewBox="0 0 12 12" aria-hidden="true"><path d="M0.5 2 H11.5 V10 H0.5 Z M1.5 3 L6 6.5 L10.5 3 Z"/></svg>dfannaby@brqholt.com</li>
        <li><svg viewBox="0 0 12 12" aria-hidden="true"><path d="M6 0.5 A5.5 5.5 0 1 0 6 11.5 A5.5 5.5 0 1 0 6 0.5 Z M6 1.8 A4.2 4.2 0 1 1 6 10.2 A4.2 4.2 0 1 1 6 1.8 Z M5.4 2 H6.6 V10 H5.4 Z M2 5.4 H10 V6.6 H2 Z"/></svg>www.brqholt.com</li>
      </ul>
    </div>
    <div class="tagline">
      <p class="tagline__line">Roland Fannaby &amp; Associates &nbsp;|&nbsp; Civil Engineering</p>
      <p class="tagline__line tagline__line--second">Land Surveying &nbsp;|&nbsp; Pipeline Integrity</p>
    </div>
  </section>

  <section class="card card--back" aria-label="Business card, brand side">
    <div class="brand"><span class="brand__name">RFA</span></div>
  </section>
</main>
</body>
</html>
```